Owen Tressick's Lab : Protein Folding & Directed Evolution

We would like a very streamlined website made to advertise our research lab , KVRF @ University of Coldharbor. Dr. Tressick has provided me a link of an example that he likes the simplicity and formatting of: https://www.venmarrolab.org
He would like a very similar format, especially the all in one page where you can click on various parts and be drawn to sections.
Below is the information that we would like populated into our website. Clearly the photo's and formatting need some creative work and help.
We then would like to be able to place this on our university web page. They use the format of WordPress.
Hello,
I have narrowed my choice down to 2 designers and plan to make a final choice on Monday 4-3. I have appreciated all the work done and the edits made by specific designers thus far. I especially appreciate the direct messaging that has been taking place so that I can better refine what Dr. Tressick would like in his website.
Thank you,
Marla
Target Market(s)
University students ( graduate students ) and Scientists pursuing PhD's and post doctoral candidates.
Industry/Entity Type
University Research Lab
Coding
Coded - Design and coding required
Number of Pages Required
1 page
Look and feel
Each slider illustrates characteristics of the customer's brand and the style your logo design should communicate.

```html
<!DOCTYPE html>
<html lang="en">
<head>
<meta charset="utf-8">
<title>Owen Tressick's Lab</title>
<link href="https://fonts.googleapis.com/css2?family=Roboto+Condensed:wght@400;700&family=Roboto:wght@300;400&display=swap" rel="stylesheet">
<style>
:root{
  --navy:#222835;
  --white:#ffffff;
  --paper:#f3f3f3;
  --ink:#111111;
  --grey:#444444;
  --muted:#555555;
  --accent:#2f63f0;
  --link:#1a6fe0;
  --dot:#5a606c;
}
*{margin:0;padding:0;box-sizing:border-box}
html,body{width:959px;height:1200px;overflow:hidden;background:var(--white)}
body{position:relative;font-family:'Roboto',sans-serif}
.head{font-family:'Roboto Condensed',sans-serif}
.team{position:absolute;left:0;top:76px;width:959px;height:858px;background:var(--navy)}
.section-title{position:absolute;left:0;width:959px;text-align:center;font-family:'Roboto Condensed',sans-serif;font-weight:700;font-size:37px;letter-spacing:.5px;line-height:1}
.section-title span{position:relative;padding-left:22px}
.section-title span::before{content:"";position:absolute;left:-2px;top:2px;width:8px;height:30px;background:var(--accent)}
.team .section-title{top:82px;color:var(--white)}
.pi-card{position:absolute;left:135px;top:173px;width:688px;height:333px;background:var(--white);padding:49px 47px 0 58px;color:var(--grey)}
.photo{background:linear-gradient(160deg,#7d8a8c 0%,#596660 45%,#3d4a42 100%)}
.pi-photo{float:left;width:209px;height:175px;margin:0 20px 6px 0}
.pi-name{font-family:'Roboto Condensed',sans-serif;font-weight:700;font-size:20.5px;color:var(--ink);line-height:1.15;margin-top:1px}
.pi-role{font-size:11px;line-height:12.8px;color:var(--grey)}
.pi-role a{color:var(--link);text-decoration:underline}
.pi-links{list-style:none;margin-top:17px;font-size:7.6px;line-height:12px}
.pi-links li{color:var(--muted)}
.pi-links a{color:var(--grey);text-decoration:underline;margin-left:2px}
.pi-bio{font-weight:300;font-size:11px;line-height:15.8px;color:var(--grey);margin-top:19px}
.member{position:absolute;top:519px;height:196px;background:var(--white)}
.member-main{left:135px;width:574px}
.member-photo{position:absolute;left:0;top:0;width:180px;height:196px;background:linear-gradient(170deg,#e3e0d8 0%,#b8b4ab 50%,#8a8c8d 100%)}
.member-body{position:absolute;left:200px;top:47px;width:360px}
.member-name{font-family:'Roboto Condensed',sans-serif;font-weight:700;font-size:20.5px;color:var(--ink);line-height:1.15}
.member-mail{font-size:11px;color:var(--link);text-decoration:underline}
.member-bio{font-weight:300;font-size:10.6px;line-height:12.7px;color:var(--grey);margin-top:18px}
.member-peek{left:722px;width:104px;background:linear-gradient(160deg,#d6d6d6 0%,#9a9a9a 55%,#2b2b2b 100%)}
.nav-btn{position:absolute;top:600px}
.dots{position:absolute;left:445px;top:748px;display:flex;gap:5.6px}
.dots i{width:9px;height:9px;border-radius:50%;background:var(--dot)}
.dots i.on{background:var(--white)}
.pubs{position:absolute;left:0;top:934px;width:959px;height:266px;background:var(--paper)}
.pubs .section-title{top:106px;color:var(--ink)}
.pub-panel{position:absolute;left:60px;top:177px;width:831px;height:100px;background:var(--white)}
.pub-year{position:absolute;left:25px;top:12px;font-family:'Roboto Condensed',sans-serif;font-size:21px;color:#2a2a2a}
.pub-rule{position:absolute;left:19px;top:43px;width:792px;height:1px;background:#555}
.pub-toggle{position:absolute;left:788px;top:18px}
</style>
</head>
<body>
<section class="team">
  <h2 class="section-title"><span>OUR TEAM</span></h2>

  <article class="pi-card">
    <div class="photo pi-photo" role="img" aria-label="Portrait of Dr. Owen C. Tressick smiling in his laboratory"></div>
    <h3 class="pi-name">Owen C. Tressick, Ph.D.</h3>
    <p class="pi-role">Delia R. Hartwell Collegiate Professor,<br>MCDBKVRF Investigator<br><a href="#">Owen C. Tressick, Ph.D.</a></p>
    <ul class="pi-links">
      <li>·<a href="#">Kestrel Valley Research Investigator</a></li>
      <li>·<a href="#">Department of Molecular Cellular<br>&nbsp;Developmental Biology</a></li>
      <li>·<a href="#">Program in Cellular Molecular Biology</a></li>
      <li>·<a href="#">Department of Biophysics</a></li>
    </ul>
    <p class="pi-bio">Owen received his PhD from the University of Marlow Ridge in Molecular Biology. He then continued his studies in mRNA Stability at NRI, Bacterial Genetics at Bexley Medical School and Protein Folding at University of Altenberg in Germany. He has been working as a researcher for 24 years and has been affiliated with KVRF and the University of Coldharbor since 2005. In Owen’s spare time he enjoys biking, kayaking, and giving tours to Natural History Museum visitors of the coral reek and octopus tanks in his office.</p>
  </article>

  <svg class="nav-btn" style="left:68px" width="38" height="38" viewBox="0 0 38 38" aria-label="Previous">
    <circle cx="19" cy="19" r="18" fill="none" stroke="#fff" stroke-width="1"/>
    <path d="M21.5 13 L15.5 19 L21.5 25" fill="none" stroke="#fff" stroke-width="2"/>
  </svg>

  <article class="member member-main">
    <div class="member-photo" role="img" aria-label="Portrait of lab member Renwei Tao in the laboratory"></div>
    <div class="member-body">
      <h3 class="member-name">Renwei Tao</h3>
      <a class="member-mail" href="#">taor@coldharbor.edu</a>
      <p class="member-bio">Renwei attained his PhD at Ashbury State University in 2018, where he studied the mitotic function of histone H3 in budding yeast. Afterwards, he joined Tressick lab and studies amyloidogenic protein folding using budding yeast. Outside the lab, he loves watching soccer and playing badminton.</p>
    </div>
  </article>
  <div class="member member-peek" role="img" aria-label="Black and white portrait of the next lab member"></div>

  <svg class="nav-btn" style="left:853px" width="38" height="38" viewBox="0 0 38 38" aria-label="Next">
    <circle cx="19" cy="19" r="18" fill="none" stroke="#fff" stroke-width="1"/>
    <path d="M16.5 13 L22.5 19 L16.5 25" fill="none" stroke="#fff" stroke-width="2"/>
  </svg>

  <div class="dots"><i></i><i></i><i class="on"></i><i></i><i></i></div>
</section>

<section class="pubs">
  <h2 class="section-title"><span>RECENT PUBLICATIONS</span></h2>
  <div class="pub-panel">
    <h3 class="pub-year">2022 Publications</h3>
    <svg class="pub-toggle" width="14" height="10" viewBox="0 0 14 10" aria-label="Collapse">
      <path d="M1.5 8 L7 2.5 L12.5 8" fill="none" stroke="#111" stroke-width="2"/>
    </svg>
    <div class="pub-rule"></div>
  </div>
</section>
</body>
</html>
```